Varnell Contracting In need of monthly newsletter

We need a monthly newsletter to promote our monthly special of Mulch Installation.

Please change wording to fit what you feel is professional and effective.

Our regular price to install Mulch is $169/Yard installed/Delivered

We would like to run a promotion of $125/Yard Installed & Delivered

Compare us to others $135/Yard Delivered only from some other suppliers

Also list somewhere on the newsletter :
- Delivery of soils, stone, wood also available
- Check out our website
- an emphasis on quality

The Fine Print
* Some Conditions apply
Mulches included in sale Onyx Velvet, Chocolate Brown, Auburn Red, Natural, Hemlock, Gold, Shredded Pine. Some site conditions may incur extra cost. minimum 3 Yards for sale price to be in effect, HST extra on all prices listed,

CHECK OUR WEBSITE FOR SOME IMAGES AND MORE INFORMATION....

ASK ANYTHING YOU WANT VIA Draft Plaza
Updates

Types of Mulch have changed Slightly in the "Fine Print"

Classic Cedar, Black Cedar, Red Cedar, Chocolate brown, Pine Bark, Natural Shredded Pine, Hemlock, Utility Style.

We will also be submitting pictures of the mulch HOWEVER you might need to crop or alter these images to make them work for our newsletter.

Project Deadline Extended
Reason: We have not yet found a design we think is Straight to the point. Simple and with our theme.

```html
<!DOCTYPE html>
<html lang="en">
<head>
<meta charset="utf-8">
<title>Varnell Contracting – Mulch Installation Sale</title>
<link rel="stylesheet" href="https://fonts.googleapis.com/css2?family=Arimo:ital,wght@0,400;0,700;1,400;1,700&display=swap">
<style>
  :root {
    --page: #ffffff;
    --ink: #111111;
    --frame: #1a1a1a;
    --lime: #8dc63f;
    --forest: #1f5a2a;
    --wood-dark: #3b2414;
    --wood-mid: #6b4326;
    --wood-light: #8a5a34;
    --garden-top: #6b7a4e;
    --garden-bottom: #4a3b30;
    --badge: #1d5f86;
    --logo: #2f6f3a;
  }
  * { box-sizing: border-box; margin: 0; padding: 0; }
  html, body {
    width: 1200px; height: 1161px; overflow: hidden;
    background: var(--page);
    font-family: "Arimo", Arial, sans-serif;
    color: var(--ink);
  }
  .flyer {
    position: absolute; left: 26px; top: 200px;
    width: 756px; height: 946px;
    border: 2px solid var(--frame);
    overflow: hidden;
    background: var(--page);
  }
  .hero {
    position: absolute; left: 0; top: 0; width: 100%; height: 267px;
  }
  .hero-wood {
    position: absolute; inset: 0;
    background: linear-gradient(180deg, var(--wood-light) 0%, var(--wood-mid) 45%, var(--wood-dark) 100%);
  }
  .hero-title {
    position: absolute; left: 38px; top: 40px;
    color: #fff; font-size: 47px; font-weight: 400; letter-spacing: -0.5px;
  }
  .hero-price {
    position: absolute; left: 38px; top: 110px;
    color: #fff; font-size: 70px; font-weight: 400; letter-spacing: -1px; line-height: 1;
  }
  .hero-sub {
    position: absolute; left: 38px; top: 184px;
    color: #fff; font-size: 31px; line-height: 1;
  }
  .hero-sub sup { font-size: 14px; }
  .hero-note {
    position: absolute; left: 38px; top: 222px;
    color: #f2e9e0; font-size: 12px;
  }
  .hero-accent {
    position: absolute; left: 438px; top: 127px;
    width: 316px; height: 114px; background: var(--lime);
  }
  .compare-band {
    position: absolute; left: 0; top: 267px; width: 100%; height: 55px;
    background: var(--forest);
    display: flex; align-items: center; justify-content: center;
    color: #fff; font-style: italic; font-size: 26px;
  }
  .garden {
    position: absolute; left: 0; top: 322px; width: 100%; bottom: 0;
    background: linear-gradient(180deg, var(--garden-top) 0%, var(--garden-bottom) 100%);
  }
  .services {
    position: absolute; left: 0; top: 623px;
    width: 332px; bottom: 0;
    background: var(--lime);
    padding: 30px 20px 0;
    text-align: center;
  }
  .services-headline {
    font-style: italic; font-size: 23px; line-height: 1.45;
  }
  .fine-print {
    margin-top: 14px;
    font-style: italic; font-size: 11px; line-height: 1.3;
  }
  .badge {
    position: absolute; left: 66px; bottom: 20px;
    width: 190px; height: 66px;
    background: var(--badge); border-radius: 4px;
  }
  .promise {
    position: absolute; left: 332px; top: 718px; right: 0; bottom: 0;
    background: var(--page);
    text-align: center;
  }
  .promise-line {
    margin-top: 24px;
    font-weight: 700; font-size: 19px; line-height: 1.35;
  }
  .brand {
    position: absolute; left: 70px; top: 106px;
    display: flex; align-items: center; gap: 14px;
  }
  .brand-dot {
    width: 54px; height: 54px; border-radius: 50%; background: var(--logo);
  }
  .brand-name {
    font-size: 30px; font-weight: 400; color: var(--logo); letter-spacing: 0.5px;
  }
  .website {
    position: absolute; left: 0; right: 0; top: 180px;
    font-size: 15px; font-weight: 700;
  }
</style>
</head>
<body>
  <main class="flyer">
    <section class="hero">
      <div class="hero-wood" role="img" aria-label="Wood planks beside shredded brown mulch"></div>
      <h1 class="hero-title">mulch installation sale</h1>
      <p class="hero-price">$125/Yard</p>
      <p class="hero-sub">Installed &amp; Delivered<sup>*</sup></p>
      <p class="hero-note">Compared to our regular $169/Yard price</p>
      <div class="hero-accent"></div>
    </section>

    <div class="compare-band">Compare with: Other suppliers charge $135/Yard delivery only</div>

    <div class="garden" role="img" aria-label="Photo of a freshly mulched front garden bed"></div>

    <aside class="services">
      <p class="services-headline">Delivery of soils, stone,<br>wood also available!</p>
      <p class="fine-print">* Some Conditions apply: Mulches included in sale Classic Cedar, Black Cedar, Red Cedar, Chocolate Brown, Pine Bark, Natural Shredded Pine, Hemlock, Utility Style. Some site conditions may incur extra cost. Minimum 3 Yards for sale price to be in effect. HST extra on all prices listed.</p>
      <div class="badge" role="img" aria-label="Accreditation badge"></div>
    </aside>

    <section class="promise">
      <p class="promise-line">First-class service, premium quality,<br>the name you can trust!</p>
      <div class="brand">
        <span class="brand-dot"></span>
        <span class="brand-name">Varnell Contracting</span>
      </div>
      <p class="website">Visit varnellcontracting.com</p>
    </section>
  </main>
</body>
</html>
```